Tumble Tap Weekly Special Flyer

Looking for a professional weekly special promotion flyer to handout. Something I can edit and use as specials change. We are a small bar in a rural town (country). Something that can be use everyday software

Tumble Tap
518 Birchgrove Lane
Wellington, Ohio 57129
(555) 318-9047
Join Us on Pagewave \Tumbletap

$1.00 Domestic Drafts every day during happy hour
Happy hour hours = Mon-Fri 3-7 Sat & Sun 12-7

Sundays:
Free Pool ALL day on both tables
$1.00 Domestic drafts until midnight

$3.00 Appetizers
$4.00 Crestvane Bloody Marys
$5.00 3 - topping pizza

Mondays:
$2.00 Well Margaritas
$3.00 7 Ferns Vodka Bombs
$4.00 Rum Runners
$6.00 Philly Cheese Steak Sandwich served with loaded fries

Tuesdays:
$2.00 Meadow Fizz
$3.00 Gray Lynx
$3.00 Loaded Nachos
$3.00 Loaded Fries
$4.00 Liquid Marijuana's

Wednesdays:
$2.00 Quiet Hollow Bottles
$3.00 Blue Stars
$3.00 Zingo Rods
$4.00 Bartender Bombs
$4.00 2 Topping Pizzas

Thursdays:
~*~*Ladies Night Thursday*~
$3.00 Tart Crumb
$3.00 Sweet Affair
$3 1/2 dozen wings!
$4.00 Spin Doctors
LADIES ONLY SPECIALS
$2.00 7 Ferns Shots
$3.00 Long Islands
$4.00 Bartender Bombs!

Fridays:
$2.00 Tavu Melora Pineapple Beer
$2.00 Lumbermill ale
$2.00 Brisk Kettle
$2.00 Wandering Pike
$3.00 Little Beers
$3.00 banana pepper rings...
$3.00 hot pepper cheese balls
$4.00 Washington Apples

Saturdays:
Extended Happy Hour (12-8)
$1.00 Domestic Drafts
$2.00 Wine Coolers
$2.00 Lumbermill Ale
$2.00 Gorbys Hard Iced Tea
$3.00 Sweet Affair
$3.00 Irish Breakfast Shots
$4.00 Irish Car Bombs
$4.00 Nova Drops
~*Until 8PM*~

add some tear off coupons that I can edit dollars and offers:
$2.00 off Pizza
$2.00 Philly Cheese Steak
Contact for us for birthday party discounts and fund raising events

attached is our company logo

I also attached a flyer of something I liked I picked up

Reason: great designs.. I need to digest them

Reason: Out of town

```html
<!DOCTYPE html>
<html lang="en">
<head>
<meta charset="utf-8">
<title>Tumble Tap Weekly Specials</title>
<link href="https://fonts.googleapis.com/css2?family=Bowlby+One&family=Open+Sans:wght@600;700&display=swap" rel="stylesheet">
<style>
:root{
  --cream:#f6ecd2;
  --panel:rgba(255,250,236,.88);
  --gold:#f2b11e;
  --amber:#e79a12;
  --red:#e31b23;
  --deep-red:#9c0d12;
  --band:#a8151b;
  --ink:#141414;
  --yellow:#ffe52b;
  --white:#ffffff;
}
*{margin:0;padding:0;box-sizing:border-box}
html,body{width:927px;height:1200px;overflow:hidden}
body{font-family:"Open Sans",Arial,sans-serif;color:var(--ink)}
.flyer{position:relative;width:927px;height:1200px;overflow:hidden;
  background:linear-gradient(180deg,var(--cream) 0%,#f3e6c6 45%,#f4d27a 62%,var(--gold) 78%,var(--amber) 100%)}
.brand-mark{position:absolute;left:40px;top:40px;width:222px;height:136px;display:flex;align-items:center;justify-content:center;gap:10px}
.brand-mark .dot{width:18px;height:18px;border-radius:50%;background:var(--deep-red)}
.brand-mark .name{font-family:"Open Sans",Arial,sans-serif;font-weight:700;font-size:30px;color:var(--deep-red)}
.title{position:absolute;left:318px;top:14px;width:580px;text-align:center;font-family:"Bowlby One",Impact,sans-serif;font-size:74px;line-height:1;color:var(--deep-red);letter-spacing:1px;white-space:nowrap}
.tagline{position:absolute;left:320px;top:116px;width:580px;text-align:center;font-weight:700;font-size:21px;white-space:nowrap}
.hours{position:absolute;left:300px;top:148px;width:600px;text-align:center;font-weight:700;font-size:23px;white-space:nowrap}
.hours .label{color:var(--red)}
.panel{position:absolute;top:195px;height:735px;background:var(--panel);border-radius:6px;padding:10px 12px 0 12px}
.panel-left{left:18px;width:437px}
.panel-right{left:473px;width:439px;padding-left:15px}
.day{margin-top:14px}
.day:first-child{margin-top:0}
.day h2{font-size:15.5px;font-weight:700;color:var(--red);line-height:22px}
.sub{font-size:14.5px;font-weight:700;color:var(--red);text-align:center;line-height:22px}
.item{display:flex;align-items:flex-end;font-size:15px;font-weight:700;line-height:22px;white-space:nowrap}
.item .leader{flex:1;border-bottom:2px dotted var(--ink);margin:0 2px 6px 3px}
.item .price{color:var(--red);font-size:16.5px}
.note{font-size:15px;font-weight:700;line-height:19px}
.coupons{margin-top:16px;text-align:center;font-weight:700;font-size:17px;line-height:21px}
.coupon-offers{margin-top:6px;text-align:center;font-weight:700;font-size:18px}
.coupon-offers .amt{color:var(--red)}
.cta{margin:8px 0 0 0;background:var(--band);color:var(--white);text-align:center;font-weight:700;font-size:16px;line-height:20px;padding:4px 6px;border:2px solid var(--white);box-shadow:0 0 0 1px var(--band)}
.until{margin-top:2px;display:flex;align-items:center;font-size:14px;font-weight:700;color:var(--red)}
.until .rule{flex:1;border-bottom:1.5px dashed var(--ink);margin:0 4px}
.photo{position:absolute;top:943px;height:150px;border:3px solid var(--deep-red);border-radius:4px}
.photo-nachos{left:188px;width:235px;background:radial-gradient(circle at 50% 55%,#f0c84a,#d98e2a 60%,#7a5a3a)}
.photo-steak{left:432px;width:235px;background:radial-gradient(circle at 50% 50%,#f1b94a,#c98a45 55%,#8a5b34)}
.photo-wings{left:677px;width:235px;background:radial-gradient(circle at 50% 55%,#e46a2c,#c4431e 55%,#f3ece2 95%)}
.glasses{position:absolute;left:0;top:934px;width:182px;height:170px;background:linear-gradient(180deg,#fffbe9 0%,#fbe9b1 18%,#f0b53a 40%,#e39613 100%);border-radius:6px 6px 0 0}
.footer{position:absolute;left:0;top:1100px;width:927px;height:100px;background:linear-gradient(180deg,#b71a20,var(--band))}
.social{position:absolute;left:182px;top:28px;color:var(--yellow);font-weight:700;font-size:20px;white-space:nowrap}
.phone{position:absolute;right:22px;top:12px;text-align:right;font-family:"Bowlby One",Impact,sans-serif;font-size:37px;line-height:1.1;color:var(--yellow);white-space:nowrap}
.address{position:absolute;left:0;top:70px;width:927px;text-align:center;color:var(--white);font-weight:700;font-size:16px}
</style>
</head>
<body>
<main class="flyer">
  <div class="brand-mark"><span class="dot"></span><span class="name">Tumble Tap</span></div>
  <h1 class="title">TUMBLE TAP</h1>
  <p class="tagline">$1.00 Domestic Drafts Every Day During Happy Hour</p>
  <p class="hours"><span class="label">Happy Hour Hours</span> = Mon-Fri 3-7 Sat &amp; Sun 12-7</p>

  <section class="panel panel-left">
    <div class="day">
      <h2>Sundays:</h2>
      <div class="item">Free Pool All Day On Both Tables</div>
      <div class="item">Domestic Drafts Until Midnight<span class="leader"></span><span class="price">$1.00</span></div>
      <div class="item">Appetizers<span class="leader"></span><span class="price">$3.00</span></div>
      <div class="item">Crestvane Bloody Marys<span class="leader"></span><span class="price">$4.00</span></div>
      <div class="item">3 - Topping Pizza<span class="leader"></span><span class="price">$5.00</span></div>
    </div>
    <div class="day">
      <h2>Mondays:</h2>
      <div class="item">Well Margaritas<span class="leader"></span><span class="price">$3.00</span></div>
      <div class="item">7 Ferns Vodka Bombs<span class="leader"></span><span class="price">$3.00</span></div>
      <div class="item">Rum Runners<span class="leader"></span><span class="price">$4.00</span></div>
      <div class="note">Philly Cheese Steak Sandwich</div>
      <div class="item">Served With Loaded Fries<span class="leader"></span><span class="price">$6.00</span></div>
    </div>
    <div class="day">
      <h2>Tuesdays:</h2>
      <div class="item">Meadow Fizz<span class="leader"></span><span class="price">$2.00</span></div>
      <div class="item">Gray Lynx<span class="leader"></span><span class="price">$3.00</span></div>
      <div class="item">loaded Nachos<span class="leader"></span><span class="price">$3.00</span></div>
      <div class="item">loaded Fries<span class="leader"></span><span class="price">$3.00</span></div>
      <div class="item">Liquid Marijuana's<span class="leader"></span><span class="price">$4.00</span></div>
    </div>
    <div class="day">
      <h2>Wednesdays:</h2>
      <div class="item">Quiet Hollow Bottles<span class="leader"></span><span class="price">$2.00</span></div>
      <div class="item">Blue Stars<span class="leader"></span><span class="price">$2.00</span></div>
      <div class="item">Zingo Rods<span class="leader"></span><span class="price">$3.00</span></div>
      <div class="item">Bartender Bombs<span class="leader"></span><span class="price">$4.00</span></div>
      <div class="item">2 Topping Pizzas<span class="leader"></span><span class="price">$4.00</span></div>
    </div>
    <p class="coupons">Add Some Tear Off Coupons That I Can Edit<br>Dollars And Offers:</p>
    <p class="coupon-offers"><span class="amt">$2.00</span> Off Pizza &bull; <span class="amt">$2.00</span> Philly Cheese Steak</p>
    <p class="cta">Contact For Us For Birthday Party Discounts<br>And Fund Raising Events</p>
  </section>

  <section class="panel panel-right">
    <div class="day">
      <h2>Thursdays:</h2>
      <div class="sub">Ladies Night Thursday</div>
      <div class="item">Tart Crumb<span class="leader"></span><span class="price">$3.00</span></div>
      <div class="item">Sweet Affair<span class="leader"></span><span class="price">$3.00</span></div>
      <div class="item">1/2 Dozen Wings!<span class="leader"></span><span class="price">$3.00</span></div>
      <div class="item">Spin Doctors<span class="leader"></span><span class="price">$4.00</span></div>
      <div class="sub">Ladies Only Specials</div>
      <div class="item">7 Ferns Shots<span class="leader"></span><span class="price">$2.00</span></div>
      <div class="item">Long Islands<span class="leader"></span><span class="price">$3.00</span></div>
      <div class="item">Bartender Bombs!<span class="leader"></span><span class="price">$4.00</span></div>
    </div>
    <div class="day" style="margin-top:26px">
      <h2>Fridays:</h2>
      <div class="item">Tavu Melora Pineapple Beer<span class="leader"></span><span class="price">$2.00</span></div>
      <div class="item">Lumbermill Ale<span class="leader"></span><span class="price">$2.00</span></div>
      <div class="item">Brisk Kettle<span class="leader"></span><span class="price">$2.00</span></div>
      <div class="item">Wandering Pike<span class="leader"></span><span class="price">$2.00</span></div>
      <div class="item">Little Beers<span class="leader"></span><span class="price">$3.00</span></div>
      <div class="item">Banana Pepper Rings<span class="leader"></span><span class="price">$3.00</span></div>
      <div class="item">Hot Pepper Cheese Balls<span class="leader"></span><span class="price">$3.00</span></div>
      <div class="item">Washington Apples<span class="leader"></span><span class="price">$4.00</span></div>
    </div>
    <div class="day" style="margin-top:32px">
      <h2>Saturdays:</h2>
      <div class="sub">Extended Happy Hour (12-8)</div>
      <div class="item">Domestic Drafts<span class="leader"></span><span class="price">$1.00</span></div>
      <div class="item">Wine Coolers<span class="leader"></span><span class="price">$2.00</span></div>
      <div class="item">Lumbermill Ale<span class="leader"></span><span class="price">$2.00</span></div>
      <div class="item">Gorbys Hard Iced Tea<span class="leader"></span><span class="price">$2.00</span></div>
      <div class="item">Sweet Affair<span class="leader"></span><span class="price">$3.00</span></div>
      <div class="item">Irish Breakfast Shots<span class="leader"></span><span class="price">$3.00</span></div>
      <div class="item">Irish Car Bombs<span class="leader"></span><span class="price">$4.00</span></div>
      <div class="item">Nova Drops<span class="leader"></span><span class="price">$4.00</span></div>
      <div class="until"><span class="rule"></span>Until 8pm<span class="rule"></span></div>
    </div>
  </section>

  <div class="glasses" role="img" aria-label="Two tall glasses of golden draft beer with foam heads"></div>
  <div class="photo photo-nachos" role="img" aria-label="Plate of loaded nachos with melted cheese, jalapeños and tomatoes"></div>
  <div class="photo photo-steak" role="img" aria-label="Philly cheese steak sandwich with melted cheese and peppers"></div>
  <div class="photo photo-wings" role="img" aria-label="Plate of buffalo chicken wings"></div>

  <footer class="footer">
    <p class="social">Join Us on Pagewave \Tumbletap</p>
    <p class="phone">(555) 318-9047</p>
    <p class="address">518 Birchgrove Lane, Wellington, Ohio 57129</p>
  </footer>
</main>
</body>
</html>
```